Business Card for my building company

I would like the card to make a statement, so as soon as you see the card you think "wow nice card' and then read the details on the card its self. Also i would like to be able to put in the detail for the MUST HAVES so please Crete a box that i can alter depending on who in my business needs the cards. Thank you

Target Market(s)

Any one looking to build a house/ townhouse or duplex

Industry/Entity Type

Home Builder

Contact Information for Business Card

I would like the card to have the logo on the card and the must haves

Font styles to use
Sans Serif

Requirements
Must have
• Name
• Phone Number
• Email Address
• Website
• Licence Number
• Abn

```html
<!DOCTYPE html>
<html lang="en">
<head>
<meta charset="utf-8">
<title>Crestline Builders – Business Card</title>
<link href="https://fonts.googleapis.com/css2?family=Open+Sans:wght@400;600&display=swap" rel="stylesheet">
<style>
  :root {
    --page-bg: #e9e6e1;
    --card-black: #050505;
    --wood-dark: #3a2f24;
    --wood-mid: #6b5a46;
    --wood-light: #8a7861;
    --gold: #c9a43a;
    --gold-soft: #d7b54a;
    --text-light: #d9d9d9;
  }
  * { margin: 0; padding: 0; box-sizing: border-box; }
  html, body {
    width: 1200px; height: 870px; overflow: hidden;
    background: var(--page-bg);
    font-family: "Open Sans", Arial, sans-serif;
  }
  .canvas { position: relative; width: 1200px; height: 870px; }
  .card {
    position: absolute; left: 360px; top: 45px;
    width: 480px; height: 780px;
    background: var(--card-black);
    overflow: hidden;
    box-shadow: 0 10px 30px rgba(0,0,0,.35);
  }
  .card-backdrop {
    position: absolute; inset: 0 0 auto 0; height: 470px;
    background:
      radial-gradient(ellipse at 50% 30%, var(--wood-light) 0%, var(--wood-mid) 45%, var(--wood-dark) 100%);
  }
  .card-wave { position: absolute; left: 0; top: 0; width: 480px; height: 780px; }
  .brand {
    position: absolute; left: 0; right: 0; top: 150px;
    display: flex; align-items: center; justify-content: center; gap: 16px;
  }
  .brand-mark {
    width: 34px; height: 34px; background: var(--gold);
  }
  .brand-name {
    font-weight: 600; font-size: 38px; color: var(--gold-soft);
    line-height: 1.1; text-align: left;
  }
  .details {
    position: absolute; left: 70px; top: 505px;
    color: var(--text-light);
  }
  .person-name {
    font-size: 30px; font-weight: 400; color: var(--gold-soft);
    margin-bottom: 18px;
  }
  .credential { font-size: 20px; line-height: 30px; }
  .contact-list { list-style: none; margin-top: 24px; }
  .contact-list li {
    display: flex; align-items: center; gap: 12px;
    font-size: 20px; line-height: 34px;
  }
  .contact-icon {
    width: 22px; height: 22px; background: var(--gold);
    display: inline-flex; align-items: center; justify-content: center;
    flex: none;
  }
</style>
</head>
<body>
<main class="canvas">
  <section class="card">
    <div class="card-backdrop" role="img" aria-label="Warm brown timber wall and floorboard backdrop"></div>
    <svg class="card-wave" viewBox="0 0 480 780" aria-hidden="true">
      <path d="M0 470 C 120 420, 300 380, 480 400 L480 780 L0 780 Z" fill="var(--card-black)"/>
      <path d="M0 470 C 120 420, 300 380, 480 400" fill="none" stroke="var(--gold)" stroke-width="4"/>
    </svg>

    <div class="brand">
      <span class="brand-mark"></span>
      <span class="brand-name">Crestline<br>Builders</span>
    </div>

    <div class="details">
      <p class="person-name">Dana Holt</p>
      <p class="credential">Lic No.4402198</p>
      <p class="credential">ABN: 12345678901</p>
      <ul class="contact-list">
        <li>
          <span class="contact-icon">
            <svg width="14" height="14" viewBox="0 0 24 24"><path d="M6.6 10.8a15 15 0 0 0 6.6 6.6l2.2-2.2a1 1 0 0 1 1-.25 11.4 11.4 0 0 0 3.6.57 1 1 0 0 1 1 1V20a1 1 0 0 1-1 1A17 17 0 0 1 3 4a1 1 0 0 1 1-1h3.5a1 1 0 0 1 1 1c0 1.25.2 2.45.57 3.57a1 1 0 0 1-.25 1z" fill="#111"/></svg>
          </span>0400 123 456
        </li>
        <li>
          <span class="contact-icon">
            <svg width="14" height="14" viewBox="0 0 24 24"><rect x="3" y="5" width="18" height="14" fill="none" stroke="#111" stroke-width="2"/><path d="M3 6l9 7 9-7" fill="none" stroke="#111" stroke-width="2"/></svg>
          </span>hello@crestline.com
        </li>
        <li>
          <span class="contact-icon">
            <svg width="14" height="14" viewBox="0 0 24 24"><circle cx="12" cy="12" r="9" fill="none" stroke="#111" stroke-width="2"/><path d="M3 12h18M12 3c3 3 3 15 0 18M12 3c-3 3-3 15 0 18" fill="none" stroke="#111" stroke-width="1.6"/></svg>
          </span>www.crestline.com
        </li>
      </ul>
    </div>
  </section>
</main>
</body>
</html>
```